ROVA Pty Ltd Business Card

Looking for a simple yet eye-catching double-sided business card design using my company logo on one side and contact details on the other.

Target Market(s)

Government

Industry/Entity Type

Communication Systems Engineering

Contact Information for Business Card

ROVA Pty Ltd

Requirements
Nice to have
• Would be great to have a QR code so details can be scanned into contacts

```html
<!DOCTYPE html>
<html lang="en">
<head>
<meta charset="utf-8">
<title>ROVA Pty Ltd Business Card</title>
<link rel="stylesheet" href="https://fonts.googleapis.com/css2?family=Montserrat:wght@400;500;600;700&display=swap">
<style>
  :root {
    --slate: #2a3a42;
    --slate-deep: #1f2c33;
    --paper: #ffffff;
    --rule-grey: #a3a3a3;
    --text-light: #e9eef0;
    --text-muted: #b9c2c6;
    --silver: #c9cdcf;
    --backdrop: #3a3a3a;
  }
  * { box-sizing: border-box; margin: 0; padding: 0; }
  html, body { width: 1200px; height: 1200px; overflow: hidden; }
  body {
    background: var(--backdrop);
    font-family: "Montserrat", sans-serif;
    display: flex;
    flex-direction: column;
    align-items: center;
    justify-content: center;
    gap: 60px;
  }
  .card {
    width: 860px;
    height: 490px;
    border-radius: 34px;
    overflow: hidden;
    position: relative;
    box-shadow: 0 14px 30px rgba(0,0,0,0.45);
  }

  /* Front: contact side */
  .card-front { background: var(--slate); }
  .front-top {
    position: absolute; left: 0; top: 0; width: 100%; height: 232px;
    background: var(--paper);
    display: flex; align-items: center; justify-content: center; gap: 26px;
  }
  .front-stripe {
    position: absolute; left: 0; top: 232px; width: 100%; height: 14px;
    background: var(--rule-grey);
  }
  .front-gap {
    position: absolute; left: 0; top: 246px; width: 100%; height: 8px;
    background: var(--paper);
  }
  .brand-mark {
    width: 64px; height: 64px; border-radius: 50%;
    background: var(--slate);
  }
  .brand-name {
    font-weight: 600; font-size: 96px; letter-spacing: 6px;
    color: var(--slate);
    line-height: 1;
  }
  .front-bottom {
    position: absolute; left: 0; top: 254px; width: 100%; height: 236px;
    display: flex; align-items: center;
  }
  .person {
    width: 400px; padding-left: 70px;
    border-right: 0;
    display: flex; gap: 14px; align-items: stretch;
  }
  .person-bar { width: 6px; background: var(--rule-grey); }
  .person-name {
    font-size: 34px; font-weight: 500; color: var(--text-light);
    letter-spacing: 1px; line-height: 1.05;
  }
  .person-role {
    font-size: 19px; font-weight: 400; color: var(--text-light);
    letter-spacing: 1px; margin-top: 4px;
  }
  .divider { width: 1px; height: 150px; background: #8c989e; }
  .contacts {
    list-style: none; padding-left: 44px;
    display: flex; flex-direction: column; gap: 10px;
  }
  .contacts li {
    display: flex; align-items: flex-start; gap: 14px;
    font-size: 21px; color: var(--text-light); line-height: 1.2;
  }
  .contacts svg { width: 22px; height: 22px; flex: none; margin-top: 2px; fill: var(--text-muted); }

  /* Back: brand side */
  .card-back {
    background: radial-gradient(ellipse at 60% 35%, #34464e 0%, var(--slate) 45%, var(--slate-deep) 100%);
    display: flex; align-items: center; justify-content: center; gap: 34px;
  }
  .card-back .brand-mark { width: 90px; height: 90px; background: var(--silver); }
  .card-back .brand-name { font-size: 130px; color: var(--silver); letter-spacing: 8px; }
</style>
</head>
<body>

<section class="card card-front" aria-label="Business card, contact side">
  <div class="front-top">
    <span class="brand-mark"></span>
    <span class="brand-name">ROVA</span>
  </div>
  <div class="front-stripe"></div>
  <div class="front-gap"></div>
  <div class="front-bottom">
    <div class="person">
      <span class="person-bar"></span>
      <div>
        <p class="person-name">FULL NAME</p>
        <p class="person-role">POSITION</p>
      </div>
    </div>
    <span class="divider"></span>
    <ul class="contacts">
      <li>
        <svg viewBox="0 0 24 24" aria-hidden="true"><path d="M6.6 10.8a15 15 0 0 0 6.6 6.6l2.2-2.2a1 1 0 0 1 1-.25 11.4 11.4 0 0 0 3.6.57 1 1 0 0 1 1 1V20a1 1 0 0 1-1 1A17 17 0 0 1 3 4a1 1 0 0 1 1-1h3.5a1 1 0 0 1 1 1c0 1.25.2 2.45.57 3.57a1 1 0 0 1-.25 1z"/></svg>
        <span>(000) 000 0000</span>
      </li>
      <li>
        <svg viewBox="0 0 24 24" aria-hidden="true"><path d="M2 5h20v14H2zM4 7v.5l8 5.5 8-5.5V7zM4 9.9V17h16V9.9l-8 5.5z"/></svg>
        <span>admin@rova.com.au</span>
      </li>
      <li>
        <svg viewBox="0 0 24 24" aria-hidden="true"><path d="M12 2a10 10 0 1 0 0 20 10 10 0 0 0 0-20zm6.9 6h-2.95a15.6 15.6 0 0 0-1.38-3.56A8 8 0 0 1 18.9 8zM12 4.04A14 14 0 0 1 13.9 8h-3.8A14 14 0 0 1 12 4.04zM4.26 14a8 8 0 0 1 0-4h3.38a16 16 0 0 0 0 4zm.82 2h2.95a15.6 15.6 0 0 0 1.38 3.56A8 8 0 0 1 5.08 16zM8.03 8H5.08a8 8 0 0 1 4.33-3.56A15.6 15.6 0 0 0 8.03 8zM12 19.96A14 14 0 0 1 10.1 16h3.8A14 14 0 0 1 12 19.96zM14.34 14H9.66a14.7 14.7 0 0 1 0-4h4.68a14.7 14.7 0 0 1 0 4zm.25 5.56A15.6 15.6 0 0 0 15.97 16h2.95a8 8 0 0 1-4.33 3.56zM16.36 14a16 16 0 0 0 0-4h3.38a8 8 0 0 1 0 4z"/></svg>
        <span>www.rova.com.au</span>
      </li>
      <li>
        <svg viewBox="0 0 24 24" aria-hidden="true"><path d="M12 2a7 7 0 0 0-7 7c0 5.25 7 13 7 13s7-7.75 7-13a7 7 0 0 0-7-7zm0 9.5A2.5 2.5 0 1 1 12 6.5a2.5 2.5 0 0 1 0 5z"/></svg>
        <span>14-16 Harlow St. Westmere<br>NSW 2150, Australia</span>
      </li>
    </ul>
  </div>
</section>

<section class="card card-back" aria-label="Business card, brand side">
  <span class="brand-mark"></span>
  <span class="brand-name">ROVA</span>
</section>

</body>
</html>
```